Sprouts at Desk

We need a logo and graphich design for a one page text for our Sprouts @desk program, it would nened to match or be inspired from our corporate indentity which can be seen at www.tolvaro-partners.com

Dear XXX
BRX is proud to launch its first ever SPROUTS @ DESK day! We invite you and your child(ren) to join us on this special day, and strengthen the connection between education and work, and your relationship between parent and child(ren).

Who? All children, all ages
Where? BRX offices
When? January 29th, from 13h – 17h

Sprouts @ Desk is the perfect time to start shaping your children’s future through education and experience at BRX with a program tailored to target each age group. There will be group activities and sessions, as well as one on one time for parents and their children.
We are excited to work together with you and your children to create a true sense of community, and celebrate the opportunities and possibilities for the next generation. It’s a day to share your passion and know-how and show what happens when you are at work. We will show children the value of education and help them discover the power and potential of a balanced work and family life. We would like to give you and your children an opportunity to express their future goals and dreams and help begin together the steps towards achieving these through the follow up with Sprouts @ Hope. BRX is developing a multi-program to enable parents and children to realize the future they dream of.
We look forward to seeing you @ Work!

```html
<!DOCTYPE html>
<html lang="en">
<head>
<meta charset="utf-8">
<title>BRX – Sprouts @ Desk stationery</title>
<link rel="stylesheet" href="https://fonts.googleapis.com/css2?family=Arimo:wght@400;700&family=Tinos:wght@400;700&display=swap">
<style>
  :root {
    --page: #ffffff;
    --paper: #f6f3ea;
    --paper-light: #fbf9f3;
    --ink: #1a1a1a;
    --brand: #c6226e;
    --brand-grey: #6d6d6d;
    --pink: #ee7fa8;
    --plum: #8e2f6a;
    --purple-dark: #4b2a5e;
    --magenta: #d5246c;
    --lilac: #b48ad6;
    --dash-purple: #7a3fc0;
    --flora-a: #e9d3e0;
    --flora-b: #d9c6e3;
  }
  * { margin: 0; padding: 0; box-sizing: border-box; }
  html, body {
    width: 706px; height: 1200px; overflow: hidden;
    background: var(--page);
  }
  .canvas { position: relative; width: 706px; height: 1200px; }

  /* Business card */
  .business-card {
    position: absolute; left: 46px; top: 34px; width: 611px; height: 290px;
    background: linear-gradient(180deg, var(--paper-light), var(--paper));
    overflow: hidden;
    box-shadow: 0 14px 14px -10px rgba(0,0,0,0.35);
  }
  .card-flourish {
    position: absolute; right: 0; top: 0; width: 150px; height: 180px;
    background: radial-gradient(ellipse at 70% 40%, rgba(225,218,196,0.7), rgba(246,243,234,0) 70%);
  }
  .card-ring {
    position: absolute; left: -30px; top: -50px; width: 165px; height: 165px;
    border: 1.5px dashed var(--pink); border-radius: 50%;
  }
  .card-waves { position: absolute; left: 0; bottom: 0; width: 611px; height: 110px; }

  .brand-mark {
    position: absolute; display: flex; align-items: center; gap: 8px;
    font-family: "Tinos", "Times New Roman", serif; font-weight: 400;
    color: var(--brand); line-height: 1;
  }
  .brand-mark .dot {
    width: 12px; height: 12px; border-radius: 50%; background: var(--brand);
  }
  .business-card .brand-mark { left: 20px; top: 22px; font-size: 56px; }

  .contact-block {
    position: absolute; left: 225px; top: 48px; width: 190px;
    font-family: "Arimo", Arial, sans-serif; text-align: center; color: var(--ink);
  }
  .contact-name { font-size: 13px; font-weight: 700; letter-spacing: 0.2px; }
  .contact-role { font-size: 11px; margin-bottom: 14px; }
  .contact-lines { font-size: 8.4px; line-height: 13px; white-space: nowrap; }

  /* Letterhead */
  .letterhead {
    position: absolute; left: 75px; top: 370px; width: 561px; height: 812px;
    background:
      radial-gradient(ellipse at 55% 40%, #ffffff 0%, var(--paper-light) 45%, var(--paper) 100%);
    overflow: hidden;
  }
  .letterhead-ring {
    position: absolute; left: -120px; top: -140px; width: 335px; height: 335px;
  }
  .letterhead .brand-mark { left: 28px; top: 30px; font-size: 62px; }

  .event-facts {
    position: absolute; left: 333px; top: 26px;
    font-family: "Tinos", "Times New Roman", serif; font-size: 13px; line-height: 14.5px; color: var(--ink);
  }
  .event-facts dt { display: inline; font-weight: 700; }
  .event-facts dd { display: inline; }
  .event-facts dd::after { content: ""; display: block; }

  .flora-left {
    position: absolute; left: 0; top: 205px; width: 108px; height: 410px;
    background: linear-gradient(160deg, var(--flora-a), var(--flora-b) 55%, rgba(233,211,224,0.4));
    border-radius: 0 60px 60px 0; opacity: 0.75;
  }
  .flora-right {
    position: absolute; right: 0; top: 445px; width: 40px; height: 240px;
    background: linear-gradient(180deg, var(--flora-b), var(--flora-a));
    border-radius: 40px 0 0 40px; opacity: 0.75;
  }

  .letter-body {
    position: absolute; left: 141px; top: 178px; width: 352px;
    font-family: "Tinos", "Times New Roman", serif; font-size: 16.2px; line-height: 19.4px;
    color: var(--ink); hyphens: auto;
  }
  .letter-body .salutation { font-weight: 700; font-size: 17px; }
  .letter-waves { position: absolute; left: 0; bottom: 0; width: 561px; height: 160px; }
</style>
</head>
<body>
<main class="canvas">

  <section class="business-card" aria-label="Business card">
    <div class="card-flourish" role="img" aria-label="Faint floral ornament in the corner"></div>
    <div class="card-ring"></div>
    <div class="brand-mark"><span>BRX</span><span class="dot"></span></div>

    <div class="contact-block">
      <p class="contact-name">YOUR NAME</p>
      <p class="contact-role">Your Position</p>
      <div class="contact-lines">
        <p>Address Line 1, Address Line 2</p>
        <p>Address Line 3, Address Line 4</p>
        <p>Tel : +00 0000 0000</p>
        <p>Fax : +00 0000 0000</p>
        <p>Email: nadia.ferrant@tolvaro-partners.com</p>
        <p>Website: www.tolvaro-partners.com</p>
      </div>
    </div>

    <svg class="card-waves" viewBox="0 0 611 110" preserveAspectRatio="none">
      <path d="M0 22 C120 58 260 58 380 28 C470 6 550 -2 611 4 L611 110 L0 110 Z" fill="var(--pink)"/>
      <path d="M0 36 C130 70 270 68 390 40 C480 18 560 12 611 16 L611 110 L0 110 Z" fill="var(--purple-dark)"/>
      <path d="M0 52 C140 90 280 80 400 56 C490 38 560 34 611 38 L611 110 L0 110 Z" fill="var(--plum)"/>
    </svg>
  </section>

  <section class="letterhead" aria-label="Sprouts @ Desk invitation letter">
    <svg class="letterhead-ring" viewBox="0 0 335 335">
      <circle cx="167.5" cy="167.5" r="162" fill="none" stroke="var(--magenta)" stroke-width="3" stroke-dasharray="10 6"/>
      <circle cx="167.5" cy="167.5" r="150" fill="none" stroke="var(--dash-purple)" stroke-width="2.5" stroke-dasharray="14 8"/>
    </svg>
    <div class="brand-mark"><span>BRX</span><span class="dot"></span></div>

    <dl class="event-facts">
      <dt>Who:</dt> <dd>All children, all ages</dd>
      <dt>Where:</dt> <dd>BRX offices</dd>
      <dt>When:</dt> <dd>January 29th, from 13h – 17h</dd>
    </dl>

    <div class="flora-left" role="img" aria-label="Floral ornament with leaves and patterned circles"></div>
    <div class="flora-right" role="img" aria-label="Small floral ornament at the edge"></div>

    <article class="letter-body">
      <p class="salutation">Dear Sir,</p>
      <p>BRX is proud to launch its first ever SPROUTS @ DESK day! We invite you and your child(ren) to join us on this special day, and strengthen the connection between education and work, and your relationship between parent and child(ren)..</p>
      <p>Sprouts @ Desk is the perfect time to start shaping your children’s future through education and experience at BRX with a program tailored to target each age group. There will be group activities and sessions, as well as one on one time for parents and their children.</p>
      <p>We are excited to work together with you and your children to create a true sense of community, and celebrate the opportunities and possibilities for the next generation. It’s a day to share your passion and know-how and show what happens when you are at work. We will show children the value of education and help them discover the power and potential of a balanced work and family life. We would like to give you and your children an opportunity to express their future goals and dreams and help begin together the steps towards achieving these through the follow up with Sprouts @ Hope. BRX is developing a multi-program to enable parents and children</p>
    </article>

    <svg class="letter-waves" viewBox="0 0 561 160" preserveAspectRatio="none">
      <circle cx="115" cy="100" r="48" fill="none" stroke="var(--lilac)" stroke-width="5" stroke-dasharray="12 7"/>
      <circle cx="115" cy="100" r="30" fill="none" stroke="#e7a6cf" stroke-width="7" stroke-dasharray="10 8"/>
      <path d="M0 70 C110 110 250 95 370 55 C450 28 520 18 561 20 L561 160 L0 160 Z" fill="var(--pink)"/>
      <path d="M0 86 C120 122 260 108 380 72 C460 48 525 40 561 42 L561 160 L0 160 Z" fill="var(--purple-dark)"/>
      <path d="M0 104 C130 140 270 124 390 92 C470 72 530 66 561 68 L561 160 L0 160 Z" fill="var(--magenta)"/>
    </svg>
  </section>

</main>
</body>
</html>
```